Referral Club PostCard/ Index Card

I need to create an Index card for a Contractor Referral Club. I already did my own door hanger which I can show you. Cost is a factor because I'm just starting my company. You guys have already created my 2 logos when I did a previous logo project so I want to use those logos and colors to create a scheme double sided postcard for my referral club attached to our some examples of other ones I've seen. So, you can 1 of 3 different design/color schemes as a basis:
1) The Black background with Blue Shield
2). The Light Blue background with the white wave (Really like this and the black one)
3). My White background blue/black business card design.
So, 3 different design/color schemes to attack?

You can also look at my website for ideas

http://www.TheLanternPointGuide.example
Updates

I have a picture of the things I want to say on BOTH sides on the Index card/[Post card. Basically, there are two versions that can be created, one with the black background/blue logo motif or one with the white/blue background logo. I bought BOTH designs in my logo contest. Actually 1 is the front of the cards and the other is the back of my card. I'm looking for creativity to get these contractors to join this referral club so I can get more leads.

I have some new logos,, icons and pdfs to submit for consideration

Target Market(s)

Drawing Other Contractors into my Professional Referral Exchange Club

Industry/Entity Type

Public Insurance Adjusting

Font styles to use
Serif
Sans Serif
Other font styles liked:
• Love Zurich font but very few people have it..It is eye drawing!!

Colors
0054AA
0677BA
7BADD7
CADEEF
E8F1F8
0094D4
00A9DD
6FCCEA
C7EBF8
E9F6FB
EE7325
F08F49
F5BC92
FAE3D3
FDF4ED

Requirements
Must have
• My Blue or Black/White color scheme to stay consistent to what Ive already had done
Nice to have
• Something that jumps off to entice them to join that I haven't thought of.

```html
<!DOCTYPE html>
<html lang="en">
<head>
<meta charset="utf-8">
<title>The Lantern Point Guide – Referral Exchange Club Card</title>
<link rel="stylesheet" href="https://fonts.googleapis.com/css2?family=Arimo:wght@400;700&family=PT+Sans:ital,wght@1,700&family=Tinos:wght@400;700&display=swap">
<style>
  :root {
    --stage: #939598;
    --ink-dark: #141414;
    --ink-mid: #3a3a3a;
    --blue-deep: #0054AA;
    --blue-mid: #0677BA;
    --blue-bright: #0094D4;
    --blue-sky: #00A9DD;
    --orange: #EE7325;
    --orange-soft: #F08F49;
    --white: #ffffff;
    --text-light: #e4e4e4;
    --text-grey: #b9b9b9;
    --text-dim: #8a8a8a;
    --footer-grey: #5a5a5a;
    --rating-red: #e0262b;
    --serif: "Tinos", "Times New Roman", serif;
    --sans: "Arimo", Arial, sans-serif;
    --italic: "PT Sans", Arial, sans-serif;
  }
  * { box-sizing: border-box; margin: 0; padding: 0; }
  html, body { width: 920px; height: 1200px; overflow: hidden; }
  body { background: var(--stage); position: relative; font-family: var(--sans); }

  .card {
    position: absolute;
    width: 672px;
    height: 446px;
    overflow: hidden;
    box-shadow: 4px 6px 10px rgba(0,0,0,0.45);
    background: var(--white);
  }
  .card--front { left: 136px; top: 118px; }
  .card--back { left: 136px; top: 645px; }

  .card__texture {
    position: absolute; inset: 0;
    background: radial-gradient(ellipse at 55% 45%, #4a4a4a 0%, #2a2a2a 45%, var(--ink-dark) 85%);
  }
  .card__waves { position: absolute; inset: 0; width: 100%; height: 100%; }
  .layer { position: absolute; left: 0; right: 0; text-align: center; }

  /* Front */
  .brand-top {
    top: 36px; font-family: var(--serif); font-weight: 700;
    font-size: 27px; color: var(--white); letter-spacing: 0.5px;
  }
  .brand-sub {
    top: 72px; display: flex; justify-content: center; align-items: center; gap: 8px;
    font-family: var(--sans); font-size: 19px; color: var(--white); letter-spacing: 1px;
  }
  .brand-sub .rule { width: 88px; height: 2px; background: var(--white); }
  .club-title {
    top: 114px; font-family: var(--sans); font-weight: 400; font-size: 41px; letter-spacing: 0.3px;
    background: linear-gradient(90deg, var(--blue-sky), var(--blue-mid));
    -webkit-background-clip: text; background-clip: text; color: transparent;
  }
  .members {
    top: 173px; font-family: var(--italic); font-style: italic; font-weight: 700;
    font-size: 17px; line-height: 24px; color: var(--white);
  }
  .join-pill {
    position: absolute; left: 135px; top: 245px; width: 412px; height: 47px;
    background: linear-gradient(180deg, var(--orange-soft), var(--orange));
    border-radius: 24px; color: var(--white);
    font-size: 19px; font-weight: 700; text-align: center; line-height: 60px;
    box-shadow: 0 2px 4px rgba(0,0,0,0.4);
  }
  .join-tab {
    position: absolute; left: 212px; top: 233px; width: 256px; height: 24px; z-index: 2;
    background: linear-gradient(180deg, #ffffff, #dcdcdc);
    border-radius: 6px;
    font-size: 15px; font-weight: 700; color: var(--ink-dark);
    text-align: center; line-height: 24px;
  }
  .accolade { top: 303px; font-size: 13px; color: var(--text-grey); }
  .call-line {
    position: absolute; left: 148px; top: 367px;
    font-family: var(--serif); font-weight: 700; font-size: 40px; line-height: 46px; color: var(--blue-mid);
  }
  .service-area {
    position: absolute; left: 160px; top: 415px;
    font-size: 15px; line-height: 18px; color: var(--footer-grey);
  }
  .rating { position: absolute; left: 558px; top: 380px; width: 92px; text-align: center; }
  .rating__title { font-size: 17px; line-height: 20px; color: var(--rating-red); }
  .rating__note { font-family: var(--serif); font-size: 8.5px; line-height: 9px; color: var(--ink-mid); }
  .rating__source { font-family: var(--serif); font-size: 5px; color: var(--text-dim); }

  .mark {
    position: absolute; display: flex; flex-direction: column; align-items: center; gap: 5px;
  }
  .mark__dot { width: 72px; height: 72px; border-radius: 50%; background: var(--blue-bright); }
  .mark__name { font-family: var(--sans); font-weight: 700; font-size: 13px; color: var(--blue-mid); text-align: center; line-height: 15px; }
  .card--front .mark { left: 18px; top: 300px; width: 122px; }
  .card--back .mark { left: 522px; top: 288px; width: 122px; }

  /* Back */
  .reasons-title {
    top: 42px; font-family: var(--serif); font-weight: 400; font-size: 29px; line-height: 39px;
    color: var(--blue-bright); letter-spacing: 0.5px;
  }
  .reasons { position: absolute; left: 43px; top: 134px; list-style: none; }
  .reason {
    display: flex; align-items: center; gap: 18px;
    font-size: 19px; line-height: 22px; color: var(--text-light); text-transform: uppercase;
  }
  .reason + .reason { margin-top: 17px; }
  .reason__num {
    flex: none; width: 33px; height: 33px; border-radius: 50%;
    border: 1.5px solid var(--orange);
    border-right-color: #6d6d6d; border-bottom-color: #6d6d6d;
    text-align: center; line-height: 30px; font-size: 19px; color: var(--white);
  }
  .reason__partner { font-weight: 700; font-size: 24px; color: var(--text-dim); text-transform: none; margin: 0 12px; }
  .offer {
    position: absolute; left: 70px; top: 393px;
    font-size: 22px; line-height: 26px; color: var(--ink-dark);
  }
</style>
</head>
<body>

<section class="card card--front" aria-label="Front of referral club card">
  <div class="card__texture" role="img" aria-label="Dark smoky backdrop of a storm-damaged home interior"></div>
  <svg class="card__waves" viewBox="0 0 672 446" preserveAspectRatio="none" aria-hidden="true">
    <defs>
      <linearGradient id="wave-blue-front" x1="0" x2="1">
        <stop offset="0" stop-color="#0094D4"/>
        <stop offset="1" stop-color="#0054AA"/>
      </linearGradient>
    </defs>
    <path d="M0,330 C180,322 360,328 460,322 C560,314 630,300 672,290 L672,446 L0,446 Z" fill="url(#wave-blue-front)"/>
    <path d="M0,334 C180,326 360,334 460,330 C560,326 630,318 672,312 L672,446 L0,446 Z" fill="#111"/>
    <path d="M0,338 C180,330 360,338 460,334 C560,332 630,324 672,318 L672,446 L0,446 Z" fill="#ffffff"/>
  </svg>

  <div class="layer brand-top">THE LANTERN POINT</div>
  <div class="layer brand-sub"><span class="rule"></span>GUIDE<span class="rule"></span></div>
  <h1 class="layer club-title">REFERAL EXCHANGE CLUB</h1>
  <p class="layer members">Public Adjusters &amp; Loss Consultants<br>Damage Assessors &amp; Certified Insurance Appraisers</p>
  <div class="join-pill">Netlink-Marcus Halden-Exchange Club</div>
  <div class="join-tab">TO JOIN CLUB CLICK:</div>
  <p class="layer accolade">Best of the South 8x since 2010</p>

  <div class="mark">
    <span class="mark__dot"></span>
    <span class="mark__name">Lantern Point</span>
  </div>
  <p class="call-line">CALL 1-800-555-0199</p>
  <p class="service-area">Servicing Florida, Georgia, Alabama and Mississippi</p>
  <div class="rating">
    <p class="rating__title">A+ Rating</p>
    <p class="rating__note">Highest Rating For<br>Public Insurance Adjusters</p>
    <p class="rating__source">(Source: state review board)</p>
  </div>
</section>

<section class="card card--back" aria-label="Back of referral club card">
  <div class="card__texture" role="img" aria-label="Dark smoky backdrop of a storm-damaged home interior"></div>
  <svg class="card__waves" viewBox="0 0 672 446" preserveAspectRatio="none" aria-hidden="true">
    <defs>
      <linearGradient id="wave-blue-back" x1="0" x2="1">
        <stop offset="0" stop-color="#0054AA"/>
        <stop offset="0.5" stop-color="#0094D4"/>
        <stop offset="1" stop-color="#00A9DD"/>
      </linearGradient>
    </defs>
    <path d="M0,324 C160,334 320,348 460,348 C570,348 630,342 672,336 L672,446 L0,446 Z" fill="url(#wave-blue-back)"/>
    <path d="M0,334 C160,343 320,356 460,356 C570,356 630,350 672,344 L672,446 L0,446 Z" fill="#111"/>
    <path d="M0,340 C160,349 320,360 460,360 C570,360 630,354 672,348 L672,446 L0,446 Z" fill="#ffffff"/>
  </svg>

  <h2 class="layer reasons-title">TOP FOUR REASONS<br>FOR JOINING THE CLUB</h2>
  <ol class="reasons">
    <li class="reason"><span class="reason__num">1</span>Exclusivity only one per industry per region</li>
    <li class="reason"><span class="reason__num">2</span>Guaranteed return referral “accountability”</li>
    <li class="reason"><span class="reason__num">3</span>$75 gift certificate <span class="reason__partner">Freshway</span>or<span class="reason__partner">Valuemart</span></li>
    <li class="reason"><span class="reason__num">4</span>Trust your client has the best local<br>public administer</li>
  </ol>

  <div class="mark">
    <span class="mark__dot"></span>
    <span class="mark__name">Lantern Point</span>
  </div>
  <p class="offer">COMPLIMENTARY POLICY &amp; CLAIM REVIEW</p>
</section>

</body>
</html>
```